International Travel Technology R&D business needs a wordpress website

We are a start up team of initially 2 individuals but plan to grow our team quickly, we have deep experience in travel technology. Our goal is to provide next generation technology research and development on behalf of our clients who are leading players in the travel technology industry. Attached our logos.

Target Market(s)

Travel Technology companies

Industry/Entity Type

Travel Industry

Coding

Coded - Design and coding required

Font styles to use
Sans Serif

Requirements
Must have
• Make use of our logo and colour scheme in the attached. Has to have a sense of adventure/ stepping into the unknown but equally must convey a sense of professionalism , we are a safe pair of hands. Sample themes are in the attachment .
Nice to have
• We have identified a theme on layoutgrove which we feel would be inspirational. We hahe attached them to help in the design as inspiration.
Should not have
• images of airplanes , hotels etc, we want to project a future image.

```html
<!DOCTYPE html>
<html lang="en">
<head>
<meta charset="utf-8">
<title>Novatrail Labs</title>
<link rel="stylesheet" href="https://fonts.googleapis.com/css2?family=Lato:wght@400;700&family=Michroma&display=swap">
<style>
:root{
  --green:#3cb34a;
  --green-dark:#2b9a3a;
  --navy:#2c2f6b;
  --ink:#222;
  --text:#555;
  --muted:#888;
  --line:#d6d6d6;
  --light:#f2f2f2;
  --footer:#2b2b2b;
  --footer-deep:#1c1c1c;
  --white:#fff;
}
*{box-sizing:border-box;margin:0;padding:0}
html,body{width:1200px;height:2582px;overflow:hidden;background:var(--white)}
body{font-family:'Lato',sans-serif;color:var(--text)}
.canvas{position:relative;width:1200px;height:2582px;overflow:hidden}
.abs{position:absolute}

/* header */
.contact-tab{left:714px;top:0;width:414px;height:31px;background:#2f2f2f;border-radius:0 0 22px 22px;display:flex;align-items:center;justify-content:space-around;color:var(--white);font-size:15px}
.contact-tab b{font-weight:700;font-size:17px}
.brand{left:100px;top:30px;display:flex;align-items:center;gap:12px}
.brand-mark{width:40px;height:40px;border-radius:50%;background:var(--green)}
.brand-name{font-family:'Lato',sans-serif;font-weight:700;font-size:28px;color:var(--green);letter-spacing:1px}
.social{display:flex;gap:9px}
.social span{width:33px;height:33px;border-radius:50%;background:var(--green);display:block}
.social.head{left:952px;top:57px}
.nav{left:0;top:112px;width:1200px;height:41px;background:var(--green)}
.nav ul{list-style:none;position:absolute;left:98px;top:0;display:flex;height:41px}
.nav li{height:41px;display:flex;align-items:center;justify-content:center;color:var(--white);font-size:15px;border-right:1px solid rgba(255,255,255,.35)}
.nav li.active{background:var(--navy)}
.nav li:last-child{border-right:none}

/* hero */
.hero{left:0;top:153px;width:1200px;height:508px;background:radial-gradient(ellipse at 50% 45%,#bfe9ff 0%,#3aa3e8 18%,#0c4fa0 42%,#061b44 72%,#020817 100%)}
.tagline{left:0;top:661px;width:1200px;height:48px;background:var(--green);color:var(--white);font-size:24px;font-weight:700;display:flex;align-items:center;justify-content:center}

/* headings */
.heading{font-family:'Michroma',sans-serif;font-size:31px;color:var(--ink);letter-spacing:2px;white-space:nowrap}
.heading em{font-style:normal;color:var(--green)}
.rule{height:2px;background:var(--line)}
.rule::after{content:"";position:absolute;left:50%;top:-7px;width:16px;height:16px;margin-left:-8px;border-radius:50%;background:#bbb}
.rule.left::after{left:18px}

.btn{background:var(--green);color:var(--white);font-weight:700;font-size:14px;display:flex;align-items:center;justify-content:center;border-radius:2px;border-bottom:3px solid var(--green-dark)}

/* about */
.about-copy{left:100px;top:836px;width:614px;font-size:13.4px;line-height:25.8px;text-align:justify}
.quote-box{left:759px;top:789px;width:341px;height:308px;border:1px solid var(--line);background:var(--white)}
.quote-ribbon{left:792px;top:778px;width:279px;height:38px;background:var(--green);color:var(--white);font-weight:700;font-size:17px;display:flex;align-items:center;justify-content:center}
.field{left:778px;width:303px;height:33px;border:1px solid #cfcfcf;background:linear-gradient(#fff,#eee);font-size:13px;color:#666;padding:8px 8px}

/* services */
.services{left:0;top:1150px;width:1200px;height:446px;background:linear-gradient(180deg,#eaeaea 0%,#dcdcdc 55%,#f0f0f0 100%)}
.svc-icon{width:114px;height:114px;border-radius:50%;background:radial-gradient(circle at 50% 40%,#4cc65a,#2a9a3a);border:5px solid #e8f5ea;box-shadow:0 2px 6px rgba(0,0,0,.25);display:flex;align-items:center;justify-content:center}
.svc{width:320px;font-size:13.4px;line-height:20px;color:#444}
.svc h3{color:var(--green);font-size:20px;font-weight:700;margin-bottom:4px}
.svc .more{display:block;margin-top:4px;color:#333}
.svc.left{text-align:right}

/* blog & testimonials */
.post-date{width:48px;height:64px;text-align:center;color:var(--white);font-weight:700}
.post-date .d{background:#2f2f2f;height:34px;font-size:20px;line-height:34px}
.post-date .m{background:var(--green);height:30px;font-size:14px;line-height:30px}
.post{width:370px;font-size:13.4px;line-height:20px}
.post h4{color:var(--ink);font-size:17px;margin-bottom:3px}
.testi-box{left:637px;top:1725px;width:463px;height:143px;border:1px solid var(--line);border-radius:4px;background:var(--white);padding:16px 18px 0 46px;font-size:12.6px;font-style:italic;line-height:20.5px;color:#444}
.quote-mark{left:650px;top:1727px;font-size:40px;color:#ccc;font-family:Georgia,serif}
.avatar{left:634px;top:1827px;width:106px;height:106px;border-radius:50%;background:linear-gradient(135deg,#d8b79a,#a67b5b);border:3px solid var(--white)}
.dots{left:940px;top:1915px;display:flex;gap:8px}
.dots span{width:20px;height:20px;border-radius:50%;background:#333;color:var(--white);font-size:11px;display:flex;align-items:center;justify-content:center}
.dots span.on{background:var(--green)}

/* partners */
.partners{left:0;top:2002px;width:1200px;height:259px;background:var(--light)}
.badge{top:2131px;width:143px;height:76px;border:1px solid #cfcfcf;border-radius:3px;background:#f7f7f7;display:flex;align-items:center;justify-content:center}
.badge i{display:block;width:60px;height:36px;border-radius:4px;background:#4a4a4a}

/* footer */
.footer{left:0;top:2261px;width:1200px;height:273px;background:var(--footer)}
.footer-panel{left:0;top:2261px;width:440px;height:273px}
.foot-head{font-family:'Michroma',sans-serif;color:var(--white);font-size:17px;letter-spacing:1px}
.foot-list{list-style:none;color:#ddd;font-size:13.4px}
.foot-list li{height:34px;display:flex;align-items:flex-start;gap:10px;line-height:20px}
.bottom{left:0;top:2534px;width:1200px;height:48px;background:var(--footer-deep);color:#ddd;font-size:13.4px;display:flex;align-items:center;justify-content:center}
.up-tab{left:103px;top:2534px;width:87px;height:48px;background:#333}
</style>
</head>
<body>
<div class="canvas">

  <!-- header -->
  <div class="abs contact-tab"><span>✉ info@novatrail-labs.com</span><b>☎ +81 555.010.2200</b></div>
  <div class="abs brand"><span class="brand-mark"></span><span class="brand-name">NOVATRAIL LABS</span></div>
  <div class="abs social head"><span></span><span></span><span></span><span></span></div>
  <nav class="abs nav">
    <ul>
      <li class="active" style="width:81px">Home</li>
      <li style="width:126px">About Us</li>
      <li style="width:145px">Our Services</li>
      <li style="width:120px">Media</li>
      <li style="width:135px">Testimonials</li>
      <li style="width:165px">Our Partners</li>
      <li style="width:90px">Blog</li>
      <li style="width:140px">Contact Us</li>
    </ul>
  </nav>

  <!-- hero -->
  <div class="abs hero" role="img" aria-label="Glowing blue digital sphere made of floating screens"></div>
  <div class="abs tagline">We Are Passionate About Travel Technology</div>

  <!-- about -->
  <h2 class="abs heading" style="left:100px;top:758px">ABOUT <em>US</em></h2>
  <div class="abs rule left" style="left:100px;top:816px;width:614px"></div>
  <p class="abs about-copy">Lorem ipsum dolor sit amet, consectetuer adipiscing elit, sed diam nonummy nibh euismod tincidunt ut laoreet dolore magna aliquam erat volutpat. Ut wisi enim ad minim veniam, quis nostrud exerci tation ullamcorper suscipit lobortis nisl ut aliquip ex ea commodo consequat. Duis autem vel eum iriure dolor in hendrerit in vulputate velit esse molestie consequat, vel illum dolore eu feugiat nulla facilisis at vero eros et accumsan et iusto odio dignissim qui blandit praesent luptatum zzril delenit augue duis dolore te feugait nulla facilisi.Lorem ipsum dolor sit amet, consectetuer adipiscing elit, sed diam nonummy nibh euismod tincidunt ut laoreet dolore magna aliquam erat volutpat. Ut wisi enim ad minim veniam, quis nostrud exerci tation ullamcorper suscipit lobortis nisl ut aliquip ex ea commodo.</p>
  <div class="abs btn" style="left:98px;top:1064px;width:117px;height:33px">Read More</div>

  <div class="abs quote-box"></div>
  <div class="abs quote-ribbon">Get A Free Quote</div>
  <div class="abs field" style="top:842px">Name</div>
  <div class="abs field" style="top:888px">Email</div>
  <div class="abs field" style="top:935px;height:81px">Massage</div>
  <div class="abs btn" style="left:778px;top:1040px;width:83px;height:31px">Submit</div>

  <!-- services -->
  <div class="abs services" role="img" aria-label="Faded grey city skyline backdrop"></div>
  <h2 class="abs heading" style="left:0;width:1200px;text-align:center;top:1198px">OUR <em>SERVICES</em></h2>
  <div class="abs rule" style="left:100px;top:1257px;width:1000px"></div>

  <div class="abs svc-icon" style="left:456px;top:1281px">
    <svg width="52" height="52" viewBox="0 0 52 52" fill="#fff"><circle cx="26" cy="12" r="7"/><circle cx="11" cy="17" r="5"/><circle cx="41" cy="17" r="5"/><rect x="18" y="21" width="16" height="22" rx="4"/><rect x="5" y="24" width="11" height="16" rx="3"/><rect x="36" y="24" width="11" height="16" rx="3"/></svg>
  </div>
  <div class="abs svc-icon" style="left:611px;top:1281px">
    <svg width="52" height="52" viewBox="0 0 52 52" fill="none" stroke="#fff" stroke-width="5" stroke-linecap="round"><circle cx="30" cy="8" r="4" fill="#fff" stroke="none"/><path d="M28 16 L24 30 L18 44 M24 30 L32 36 L34 46 M26 20 L36 26"/><rect x="8" y="32" width="9" height="12" rx="2" fill="#fff" stroke="none"/></svg>
  </div>
  <div class="abs svc-icon" style="left:456px;top:1427px">
    <svg width="56" height="56" viewBox="0 0 56 56"><circle cx="22" cy="32" r="12" fill="none" stroke="#fff" stroke-width="9" stroke-dasharray="5 4"/><circle cx="22" cy="32" r="9" fill="#fff"/><circle cx="22" cy="32" r="4" fill="#2f9f3f"/><circle cx="40" cy="14" r="7" fill="none" stroke="#fff" stroke-width="6" stroke-dasharray="3.5 3"/><circle cx="40" cy="14" r="5" fill="#fff"/><circle cx="40" cy="14" r="2" fill="#2f9f3f"/></svg>
  </div>
  <div class="abs svc-icon" style="left:611px;top:1427px">
    <svg width="52" height="52" viewBox="0 0 52 52"><circle cx="26" cy="26" r="16" fill="none" stroke="#fff" stroke-width="10" stroke-dasharray="6 4.5"/><circle cx="26" cy="26" r="13" fill="#fff"/><circle cx="26" cy="26" r="5" fill="#2f9f3f"/></svg>
  </div>

  <div class="abs svc left" style="left:100px;top:1287px"><h3>Consolidators</h3>Lorem ipsum dolor sit amet, consectetuer adipiscing sed diam nonummy nibh euismod tincidunt umagna .gdag aliquam erat volutpat. tincidunt ut laoreetfgf<span class="more">Read More &gt;&gt;</span></div>
  <div class="abs svc" style="left:779px;top:1287px"><h3>Travel Agencies</h3>Lorem ipsum dolor sit amet, consectetuer adipiscing sed diam nonummy nibh euismod tincidunt umagna gdag aliquam erat volutpat. tincidunt ut laoreetfgf.<span class="more">Read More &gt;&gt;</span></div>
  <div class="abs svc left" style="left:100px;top:1429px"><h3>Technology Research</h3>Lorem ipsum dolor sit amet, consectetuer adipiscing sed diam nonummy nibh euismod tincidunt umagna .gdag aliquam erat volutpat. tincidunt ut laoreetfgf<span class="more">Read More &gt;&gt;</span></div>
  <div class="abs svc" style="left:779px;top:1429px"><h3>Development</h3>Lorem ipsum dolor sit amet, consectetuer adipiscing sed diam nonummy nibh euismod tincidunt umagna gdag aliquam erat volutpat. tincidunt ut laoreetfgf.<span class="more">Read More &gt;&gt;</span></div>

  <!-- blog -->
  <h2 class="abs heading" style="left:100px;top:1644px">LATEST <em>BLOG</em></h2>
  <div class="abs rule left" style="left:100px;top:1702px;width:440px"></div>
  <div class="abs" style="left:582px;top:1660px;width:1px;height:290px;background:var(--line)"></div>

  <div class="abs post-date" style="left:100px;top:1730px"><div class="d">24</div><div class="m">AUG</div></div>
  <div class="abs post" style="left:161px;top:1732px"><h4>Lorem Ipsum Dolor Sit Amet</h4>Lorem ipsum dolor sit amet, sed diam nonummy nibh euismod tincidunt ut laoreet dolore. Sit amet, sed diam nonu</div>
  <div class="abs" style="left:161px;top:1812px;width:370px;height:1px;background:var(--line)"></div>
  <div class="abs post-date" style="left:100px;top:1827px"><div class="d">24</div><div class="m">AUG</div></div>
  <div class="abs post" style="left:161px;top:1829px"><h4>Lorem Ipsum Dolor Sit Amet</h4>Lorem ipsum dolor sit amet, sed diam nonummy nibh euismod tincidunt ut laoreet dolore. Sit amet, sed diam nonu</div>
  <div class="abs btn" style="left:98px;top:1918px;width:102px;height:31px">View All</div>

  <!-- testimonials -->
  <h2 class="abs heading" style="left:623px;top:1644px">CLIENT <em>TESTIMONIALS</em></h2>
  <div class="abs rule left" style="left:623px;top:1702px;width:477px"></div>
  <div class="abs testi-box">Lorem ipsum dolor sit amet, sed diam nonummy nibh euismod tincidunt ut laoreet dolore. Lorem ipsum dolor sit amet, sed diam nonummy nibh euismod tincidunt ut laoreet dolore. Lorem ipsum dolor sit amet, sed diam nonummy nibh euismod tincidunt ut laoreet dolore.</div>
  <div class="abs quote-mark">“</div>
  <div class="abs" style="left:742px;top:1832px;font-size:15px;color:var(--ink)">Dana Forsyth</div>
  <div class="abs" style="left:862px;top:1832px;font-size:15px;color:var(--ink);border-left:1px solid #999;padding-left:10px">Customer</div>
  <div class="abs avatar" role="img" aria-label="Customer portrait"></div>
  <div class="abs" style="left:694px;top:1892px;width:42px;height:42px;border-radius:50%;background:#ddd;color:#555;font-family:Georgia,serif;font-size:28px;text-align:center;line-height:50px">”</div>
  <div class="abs dots"><span class="on">1</span><span>2</span><span>3</span><span>4</span></div>

  <!-- partners -->
  <div class="abs partners"></div>
  <h2 class="abs heading" style="left:0;width:1200px;text-align:center;top:2050px">OUR <em>PARTNERS</em></h2>
  <div class="abs rule" style="left:100px;top:2106px;width:1000px"></div>
  <div class="abs badge" style="left:100px"><i></i></div>
  <div class="abs badge" style="left:270px"><i></i></div>
  <div class="abs badge" style="left:442px"><i></i></div>
  <div class="abs badge" style="left:613px"><i></i></div>
  <div class="abs badge" style="left:785px"><i></i></div>
  <div class="abs badge" style="left:957px"><i></i></div>

  <!-- footer -->
  <div class="abs footer"></div>
  <svg class="abs footer-panel" viewBox="0 0 440 273" width="440" height="273"><polygon points="0,0 440,0 358,273 0,273" fill="#3cb34a"/><line x1="440" y1="0" x2="358" y2="273" stroke="#fff" stroke-width="3"/></svg>
  <div class="abs" style="left:150px;top:2330px;display:flex;align-items:center;gap:10px"><span style="width:30px;height:30px;border-radius:50%;background:#fff;display:block"></span><span style="font-weight:700;font-size:24px;color:#fff;letter-spacing:1px">NOVATRAIL LABS</span></div>
  <div class="abs social" style="left:155px;top:2453px"><span style="background:#fff"></span><span style="background:#fff"></span><span style="background:#fff"></span><span style="background:#fff"></span></div>

  <h3 class="abs foot-head" style="left:482px;top:2302px">CONTACT ADDRESS</h3>
  <div class="abs" style="left:482px;top:2334px;width:300px;height:1px;background:#555"></div>
  <ul class="abs foot-list" style="left:482px;top:2350px;width:280px">
    <li style="height:50px"><span>⌖</span><span>Lorem ipsum dolor sitamet, consectetuer adipiscing sed diam nonummy.</span></li>
    <li><span>☎</span><span>555.010.2201</span></li>
    <li><span>⎙</span><span>555.010.2202</span></li>
    <li><span>✉</span><span>info@novatrail-labs.com</span></li>
  </ul>

  <h3 class="abs foot-head" style="left:838px;top:2302px">QUICK LINKS</h3>
  <div class="abs" style="left:838px;top:2334px;width:262px;height:1px;background:#555"></div>
  <ul class="abs foot-list" style="left:838px;top:2348px">
    <li>› Home</li><li>› About Us</li><li>› Our Services</li><li>› Media</li><li>› Testimonials</li>
  </ul>
  <ul class="abs foot-list" style="left:974px;top:2348px">
    <li>› Our Partners</li><li>› Blog</li><li>› Contact Us</li>
  </ul>

  <div class="abs bottom">Copyright © 2016 Novatrail Labs . All Right Reserved.</div>
  <div class="abs up-tab"><svg width="87" height="48" viewBox="0 0 87 48"><polyline points="35,29 43,21 51,29" fill="none" stroke="#fff" stroke-width="3"/></svg></div>

</div>
</body>
</html>
```